MOLVT Study flyer

I need help designing a flyer for a research study that will include brain imaging in adolescents. The info is in the attached document. The study is called the Marrowby Orchard Lantern Vesper Trail (MOLVT) study. Ideally this would be returned as a document that I can edit in the future as we will have several new recruitment phases (different age groups, etc. I also would love to have a logo designed as part of this project, but I recognize that might be a separate design request.

```html
<!DOCTYPE html>
<html lang="en">
<head>
<meta charset="utf-8">
<title>MOLVT Study Flyer</title>
<link rel="stylesheet" href="https://fonts.googleapis.com/css2?family=Poppins:ital,wght@0,300;0,700;0,800;1,900&display=swap">
<style>
  :root {
    --sky: #80c3ca;
    --peach: #f6a96f;
    --sage: #858a74;
    --teal: #1d7773;
    --navy: #1d4877;
    --ink: #1f3b5c;
    --white: #ffffff;
    --cream: #f4ead5;
  }
  * { box-sizing: border-box; margin: 0; padding: 0; }
  html, body { width: 1200px; height: 1200px; overflow: hidden; background: var(--white); }
  body { font-family: "Poppins", sans-serif; position: relative; }

  .flyer { position: absolute; left: 198px; top: 29px; width: 812px; height: 1149px; background: var(--sky); overflow: hidden; }

  .headline { position: absolute; left: 0; width: 100%; display: flex; align-items: center; justify-content: flex-end; padding-right: 16px; color: var(--white); font-weight: 800; letter-spacing: -0.06em; white-space: nowrap; }
  .headline--parent { top: 63px; height: 64px; background: var(--peach); font-size: 41px; }
  .headline--worry { top: 138px; height: 54px; background: var(--sage); font-size: 31px; }

  .intro { position: absolute; top: 212px; left: 80px; width: 700px; text-align: center; color: var(--white); font-weight: 800; font-size: 18.5px; line-height: 23px; letter-spacing: -0.05em; text-shadow: 1px 1px 0 var(--ink), -1px 1px 0 var(--ink), 1px -1px 0 var(--ink), -1px -1px 0 var(--ink); }

  .tag { position: absolute; left: 256px; width: 320px; height: 24px; display: flex; align-items: center; justify-content: center; color: var(--white); font-weight: 800; font-size: 17px; letter-spacing: -0.04em; text-shadow: 1px 1px 0 var(--ink); }
  .tag--involves { top: 306px; background: var(--peach); }
  .tag--eligible { top: 594px; background: var(--sage); }

  .band { position: absolute; left: 0; width: 100%; }
  .band--steps { top: 342px; height: 233px; background: var(--teal); }
  .band--criteria { top: 639px; height: 179px; background: var(--navy); }

  .item { position: absolute; text-align: center; color: var(--white); font-weight: 300; font-size: 13.5px; line-height: 16.5px; letter-spacing: -0.03em; }
  .badge { position: absolute; width: 110px; height: 110px; border-radius: 50%; display: flex; align-items: center; justify-content: center; }
  .band--steps .badge { background: var(--navy); top: 16px; }
  .band--criteria .badge { background: var(--teal); top: 9px; }

  .scene { position: absolute; left: 290px; top: 808px; width: 348px; height: 272px; border-radius: 8px; background: linear-gradient(160deg, #f3c79a 0%, #e4eedb 55%, #c8676e 100%); opacity: .9; }
  .floor-line { position: absolute; left: 232px; top: 1078px; width: 346px; height: 3px; background: var(--peach); }

  .pay { position: absolute; left: 611px; top: 870px; width: 175px; height: 62px; background: var(--peach); border-radius: 14px; display: flex; flex-direction: column; align-items: center; justify-content: center; color: var(--navy); font-weight: 900; font-style: italic; font-size: 20px; line-height: 22px; letter-spacing: -0.05em; text-shadow: 1px 1px 0 var(--white); }

  .contact { position: absolute; left: 0; width: 100%; text-align: center; color: var(--white); font-weight: 800; letter-spacing: -0.05em; text-shadow: 1px 1px 0 var(--ink), -1px 1px 0 var(--ink), 1px -1px 0 var(--ink), -1px -1px 0 var(--ink); }
  .contact--ask { top: 1058px; font-size: 18.5px; }
  .contact--email { top: 1104px; font-size: 18.5px; }
</style>
</head>
<body>
<main class="flyer">
  <h1 class="headline headline--parent">Are you the parent of a child age 10-17?</h1>
  <h2 class="headline headline--worry">Do they worry or overthink negative emotions?</h2>

  <p class="intro">Halvern University researchers are seeking girls age 10-17 for a study about brain activity in emotions and decision-making and how they relate to puberty, anxiety and depression</p>

  <div class="tag tag--involves">STUDY PARTICIPATION INVOLVES:</div>

  <section class="band band--steps">
    <div class="badge" style="left:72px">
      <svg width="70" height="70" viewBox="0 0 70 70" fill="none" stroke="#fff" stroke-width="2.5" aria-hidden="true">
        <circle cx="20" cy="30" r="7"/><path d="M8 62v-12a12 12 0 0 1 24 0v12"/>
        <circle cx="48" cy="38" r="7"/><path d="M36 62a12 12 0 0 1 24 0"/>
        <rect x="34" y="6" width="20" height="14" rx="7"/><rect x="48" y="10" width="16" height="12" rx="6"/>
      </svg>
    </div>
    <p class="item" style="left:50px;top:158px;width:160px">- One one-hour interview (online or in-person) where your child will discuss their thoughts</p>

    <div class="badge" style="left:351px">
      <svg width="72" height="72" viewBox="0 0 72 72" fill="none" stroke="#fff" stroke-width="2.5" aria-hidden="true">
        <rect x="6" y="14" width="44" height="32" rx="2"/><path d="M28 46v8M18 56h20"/>
        <circle cx="22" cy="30" r="7"/><rect x="40" y="6" width="24" height="16" rx="2"/>
        <circle cx="50" cy="44" r="7"/><path d="M38 66a12 12 0 0 1 24 0"/>
      </svg>
    </div>
    <p class="item" style="left:322px;top:189px;width:170px">- Online questionnaires (parent and child)</p>

    <div class="badge" style="left:624px">
      <svg width="74" height="74" viewBox="0 0 74 74" fill="none" stroke="#fff" stroke-width="2.5" aria-hidden="true">
        <rect x="38" y="6" width="28" height="18" rx="2"/><path d="M42 15h6l3-5 3 9 3-4h5"/>
        <path d="M22 66V42a14 14 0 0 1 0-28" /><circle cx="22" cy="42" r="8"/>
        <rect x="28" y="44" width="40" height="8" rx="3"/><path d="M36 52l-8 14M4 68h60"/>
      </svg>
    </div>
    <p class="item" style="left:555px;top:130px;width:245px">- One two-hour visit where your child will complete an MRI scan, answer questions about their puberty stage, and have a small hair sample taken to study puberty hormones</p>
  </section>

  <div class="tag tag--eligible">STUDY PARTICIPATION INVOLVES:</div>

  <section class="band band--criteria">
    <div class="badge" style="left:72px">
      <svg width="76" height="70" viewBox="0 0 76 70" fill="none" stroke="#fff" stroke-width="2.5" aria-hidden="true">
        <path d="M6 20l56-12M54 4l8 4-5 7"/>
        <circle cx="14" cy="38" r="5"/><circle cx="38" cy="34" r="6"/><circle cx="62" cy="30" r="7"/>
        <path d="M4 62v-8a10 10 0 0 1 20 0v8zM26 62v-10a12 12 0 0 1 24 0v10zM50 62v-12a12 12 0 0 1 24 0v12z"/>
      </svg>
    </div>
    <p class="item" style="left:60px;top:131px;width:140px">- Are age 10-17</p>

    <div class="badge" style="left:358px">
      <svg width="72" height="76" viewBox="0 0 72 76" fill="none" stroke="#fff" stroke-width="2.5" aria-hidden="true">
        <path d="M26 10l3 6M36 4v8M46 10l-3 6"/>
        <circle cx="36" cy="32" r="11"/>
        <path d="M14 44c-10-6-4-20 8-16M58 44c10-6 4-20-8-16M18 48h36M20 48v22h32V48"/>
      </svg>
    </div>
    <p class="item" style="left:300px;top:130px;width:220px">- Tend to worry or overthink negative thoughts</p>

    <div class="badge" style="left:624px;top:4px">
      <svg width="80" height="80" viewBox="0 0 80 80" fill="none" stroke="#fff" stroke-width="2.5" aria-hidden="true">
        <rect x="10" y="26" width="52" height="50"/><path d="M36 26v50M10 51h52"/>
        <rect x="48" y="6" width="24" height="24" transform="rotate(40 60 18)"/>
      </svg>
    </div>
    <p class="item" style="left:575px;top:126px;width:205px">- have not been diagnosed with psychosis, learning problems, or autism</p>
  </section>

  <div class="scene" role="img" aria-label="Illustration of a parent standing and talking with another parent and a daughter seated on a sofa"></div>
  <div class="floor-line"></div>

  <div class="pay"><span>COMPENSATION</span><span>UP TO $140</span></div>

  <p class="contact contact--ask">Interested in participating? Want more information? Please contact us!</p>
  <p class="contact contact--email">molvtstudy@halvernhealth.edu</p>
</main>
</body>
</html>
```